Landing Page für B2B-Softwareentwicklungsfirma
Zielgruppe
Wir sind eine (relativ kleine) B2B Softwareentwicklungsfirma, die Software zum Wetten auf Pferderennen erstellt.
Unsere Kunden sind Buchmacher und Rennbahnbetreiber.
Unsere Software läuft auf verschiedener Hardware (Touchscreen Terminals, Handy, Kassa, Webseite,...) und wird teilweise von Endkunden (Sportwetter) als auch Kunden-Mitarbeitern verwendet.
Was uns von anderen Softwarefirmen in diesem Bereich unterscheidet ist:
- Wir sind extrem verlässlich und unsere Software läuft störungsfrei
- Wir haben extrem viel Knowhow und ein großes Netzwerk im Bereich Pferdesport/-wetten
- Wir sind flexibel, gehen auf Kundenwünsche immer schnell und kosteneffizient ein
- Unsere softwaretechnischen Fähigkeiten sind ausgezeichnet (wir sind hauptsächlich Programmierer - weniger Businessleute).
- Wir sind für unsere Kunden immer persönlich, direkt und einfach ansprechbar (kleine Firma)
- Wir sind seit ca 15 Jahren erfolgreich im Markt, und auch Marktführer im deutschsprachigen Raum
- Wir haben ein sehr breites Produktportfolio (Terminal, Kassa, Mobile Webseite, Desktop Webseite, Backoffice, Risk Management)
- Wir legen viel Wert auf sauberes und auch modernes UI/UX-Design
Wir benötigen nun einen professionellen Webauftritt um in neue Märkte einzutreten.
Als ersten Schritt möchten wir gerne eine Single-Page Landingpage, die alle wichtigen Punkte im Überblick darstellt.
Aufgabenstellung
Das Design soll die Punkte aus der obigen Beschreibung über uns widerspiegeln, und auch unsere Werte:
Wichtig: Modern, Verlässlichkeit, Dynamisch, Kosteneffizient, Freundlich
Optional: Kreativ, Flexibilität
Wichtig ist auch der Bezug zum Pferderennsport!
Und dass wir eine B2B Softwarefirma sind!
Bitte beachten Sie unser neues Firmenlogo - siehe Anhang.
Die Landingpage soll eher hell, klar, offen, freundlich, sachlich sein.
Die Landingpage soll auf Mobile und Desktop funktionieren und gut aussehen.
Bitte verwenden Sie folgende Gliederung der Landingpage:
Sections:
....* Above the fold
........headline: horse betting software
........subheadline: Multi-product betting solution for bookmakers and racetrack operators.
................................Software production for land-based operations and online betting.
........call-to-action: get in touch
........secondary call-to-action: view products
........switch language
........links to other sections
....* Products
........Point of Sale
............Title: Quick and streamlined bet placement
............Short desc: Optimized bet placement solution for your bet shops and race tracks. Supports Orvane-based touchscreen terminals and many different printers and scanners out of the box.
........Self-Service Terminals
............Title: Let users take control
............Short desc: Easy to use touchscreen software for new and professional punters. Running on any Orvane-based hardware and adapted to your special needs.
........Web and Mobile Betting
............Title: Reach your target audience wherever they are
............Short desc: Allow your customers to enter their bets on any desktop or mobile browser.
........Bet Management
............Title: Stay in control of your meetings and bets
............Short desc: Browser-based Back-Office solution to control all your meetings,..

```html
<!DOCTYPE html>
<html lang="en">
<head>
<meta charset="utf-8">
<title>brightmoor – Horse Betting Software Provider</title>
<link rel="stylesheet" href="https://fonts.googleapis.com/css2?family=Barlow:wght@400;500;600&family=Open+Sans:wght@400;600&display=swap">
<style>
  :root{
    --bg:#e8e6e7;
    --navy:#0b4f82;
    --blue:#1f6fa3;
    --teal:#3aa1c6;
    --cyan:#35b6d8;
    --ink:#1d3f5e;
    --muted:#6b7b88;
    --white:#ffffff;
    --sky:#e2f2f8;
    --panel-grey:#f4f4f4;
    --chip:#eef7fb;
  }
  *{box-sizing:border-box;margin:0;padding:0}
  html,body{width:1200px;height:667px;overflow:hidden;background:var(--bg)}
  body{font-family:"Open Sans",sans-serif;color:var(--ink)}
  .stage{display:flex;gap:14px;padding:0 20px;align-items:center;height:667px}
  .panel{position:relative;width:376px;height:320px;overflow:hidden;box-shadow:0 10px 30px rgba(0,0,0,.08)}

  /* About */
  .about{background:linear-gradient(160deg,#e6f4f9 0%,var(--sky) 60%,#f3fafc 100%)}
  .about-phone{position:absolute;left:50px;top:40px;width:80px;height:150px;border-radius:14px;
    background:linear-gradient(160deg,#1a2444,#0a0f22);transform:rotate(-22deg)}
  .about-copy{position:absolute;left:178px;top:42px;width:178px}
  .about-title{font-family:"Barlow",sans-serif;font-weight:500;font-size:15px;line-height:1.2;color:var(--blue)}
  .about-title span{display:block;color:var(--cyan)}
  .about-copy p{font-size:4.6px;line-height:1.6;color:var(--muted);margin-top:7px}

  /* Hero */
  .hero{background:linear-gradient(120deg,var(--navy) 0%,#1e6ea3 55%,var(--teal) 100%)}
  .nav{position:absolute;top:12px;left:30px;right:30px;display:flex;align-items:center;font-size:4.6px;color:var(--white);font-weight:600}
  .brand{display:flex;align-items:center;gap:4px;font-family:"Barlow",sans-serif;font-weight:500;font-size:10px;letter-spacing:.5px;margin-right:34px}
  .brand i{width:7px;height:7px;border-radius:50%;background:var(--cyan);display:block}
  .nav ul{display:flex;gap:8px;list-style:none}
  .nav .lang{margin-left:auto}
  .hero-head{position:absolute;top:70px;left:0;right:0;text-align:center;color:var(--white)}
  .hero-head h1{font-family:"Barlow",sans-serif;font-weight:500;font-size:22px;line-height:1.1}
  .hero-head p{font-size:5.2px;line-height:1.8;margin-top:8px}
  .cta{display:flex;gap:4px;justify-content:center;margin-top:10px}
  .btn{font-size:4.6px;font-weight:600;padding:4px 10px;color:var(--white);border:1px solid var(--white)}
  .btn-primary{background:var(--navy);border-color:var(--navy)}
  .hero-lower{position:absolute;left:0;right:0;bottom:0;height:130px;background:var(--white);
    clip-path:polygon(0 55%,100% 0,100% 100%,0 100%)}
  .devices{position:absolute;left:45px;bottom:0;width:150px;height:72px;border-radius:4px 4px 0 0;
    background:linear-gradient(135deg,#dfe7ec,#9fb8c7)}
  .products-head{position:absolute;left:216px;bottom:16px}
  .products-head h2{font-family:"Barlow",sans-serif;font-weight:500;font-size:12px;color:var(--blue)}
  .products-head h2 span{color:var(--cyan)}
  .products-head p{font-size:3.6px;color:var(--muted);margin-top:3px}

  /* Products */
  .products{background:var(--panel-grey)}
  .card{position:absolute;background:var(--white);box-shadow:0 2px 8px rgba(0,0,0,.12);padding-bottom:8px}
  .card-terminal{left:20px;top:44px;width:162px}
  .card-pos{left:192px;top:8px;width:168px}
  .card-media{height:76px;background:linear-gradient(150deg,#5a4634,#2a3340 60%,#1c2b44)}
  .card-pos .card-media{height:82px;background:linear-gradient(150deg,#8a7a66,#3b4a58 60%,#2a3a4a)}
  .card-body{padding:6px 6px 0}
  .tag{display:inline-block;font-size:3.6px;background:var(--chip);color:var(--blue);padding:2px 5px}
  .card h3{font-family:"Barlow",sans-serif;font-weight:500;font-size:7px;color:var(--ink);margin-top:6px}
  .card h3 span{color:var(--cyan)}
  .card-pos h3{color:var(--cyan)}
  .card-pos h3 span{color:var(--ink)}
  .card p{font-size:3.6px;line-height:1.8;color:#3b4550;margin-top:4px}
  .chips{display:flex;gap:4px;margin-top:6px}
  .chip{display:flex;align-items:center;gap:2px;font-size:3.2px;color:var(--blue);background:var(--chip);padding:3px 4px}
  .chip svg{width:5px;height:5px}
  .details{display:inline-block;font-size:3.8px;color:var(--blue);border:1px solid var(--blue);padding:2px 5px;margin-top:6px}
  .card-race{position:absolute;left:192px;top:256px;width:168px;height:70px;background:linear-gradient(180deg,#7a2a2a,#3a3030)}
</style>
</head>
<body>
<main class="stage">

  <section class="panel about">
    <div class="about-phone" role="img" aria-label="Smartphone showing the horse betting app start screen"></div>
    <div class="about-copy">
      <h2 class="about-title">Pioneering the Future of <span>Horse Racing Betting</span><span>Software</span></h2>
      <p>As a specialized B2B software firm, we have served the horse racing betting industry for over 15 years, building versatile software for bookmakers and racetrack operators on terminals, mobile devices and websites.</p>
      <p>Our distinction comes from reliable software and deep knowledge of horse racing. Our team of programmers focuses on flexibility and technical excellence, adapting quickly to client needs.</p>
      <p>Despite our growth we keep a small-company feel with direct, personal client relationships and a product range from terminals to risk management tools.</p>
      <p>As we enter new markets, we stay committed to reliable software for the dynamic world of horse racing betting.</p>
    </div>
  </section>

  <section class="panel hero">
    <nav class="nav">
      <div class="brand"><i></i>brightmoor</div>
      <ul><li>Products</li><li>Why choose us?</li><li>Company</li><li>FAQ</li></ul>
      <ul class="lang"><li>Contact Us</li><li>English</li><li>German</li></ul>
    </nav>
    <div class="hero-head">
      <h1>Horse Betting<br>Software Provider</h1>
      <p>Multi-product betting solution for bookmakers and racetrack operators.<br>Software solutions for land-based operations and online betting.</p>
      <div class="cta"><span class="btn btn-primary">Get in Touch</span><span class="btn">View Products</span></div>
    </div>
    <div class="hero-lower"></div>
    <div class="devices" role="img" aria-label="Desktop and phone screens showing the betting interface"></div>
    <div class="products-head">
      <h2>Our <span>Products</span></h2>
      <p>Lorem ipsum dolor sit amet, consectetur adipiscing elit sed</p>
    </div>
  </section>

  <section class="panel products">
    <article class="card card-terminal">
      <div class="card-media" role="img" aria-label="Self-service betting terminal in a lounge"></div>
      <div class="card-body">
        <span class="tag">Self-Service Terminals</span>
        <h3>Let users enter their <span>bets themselves</span></h3>
        <p>Easy to use touchscreen software for new and professional punters.<br>Running on any Orvane-based hardware and adapted to your special needs.</p>
        <div class="chips">
          <span class="chip"><svg viewBox="0 0 10 10"><rect x="1" y="1" width="8" height="8" fill="none" stroke="currentColor"/></svg>Horse Betting Software</span>
          <span class="chip"><svg viewBox="0 0 10 10"><rect x="1" y="1" width="8" height="8" fill="none" stroke="currentColor"/></svg>Cashier System</span>
          <span class="chip"><svg viewBox="0 0 10 10"><rect x="1" y="1" width="8" height="8" fill="none" stroke="currentColor"/></svg>Terminal Software</span>
        </div>
        <span class="details">View Details</span>
      </div>
    </article>
    <article class="card card-pos">
      <div class="card-media" role="img" aria-label="Point of sale screen in a betting shop"></div>
      <div class="card-body">
        <span class="tag">Point of Sale</span>
        <h3>Quick and streamlined <span>bet placement</span></h3>
        <p>Optimized bet placement solution for your bet shops and race tracks.<br>Supports Orvane-based touchscreen terminals and many different printers and scanners out of the box.</p>
        <div class="chips">
          <span class="chip"><svg viewBox="0 0 10 10"><rect x="1" y="1" width="8" height="8" fill="none" stroke="currentColor"/></svg>Horse Betting Software</span>
          <span class="chip"><svg viewBox="0 0 10 10"><rect x="1" y="1" width="8" height="8" fill="none" stroke="currentColor"/></svg>Cashier System</span>
          <span class="chip"><svg viewBox="0 0 10 10"><rect x="1" y="1" width="8" height="8" fill="none" stroke="currentColor"/></svg>Terminal Software</span>
        </div>
        <span class="details">View Details</span>
      </div>
    </article>
    <div class="card-race" role="img" aria-label="Live race broadcast with odds overlay"></div>
  </section>

</main>
</body>
</html>
```